Sheriff Candidate needs a large yard sign

A candidate for Sheriff needs to have a sign to put in front of businesses and houses that advertise her candidacy.

Target Market(s)

Democrats, voters

Industry/Entity Type

Political

Font styles to use
Sans Serif

Colors
34a7d7
3276b5

Requirements
Must have
• Must have her picture
• Must have the words "Elect Dana Whitlock" - I'd like the name Dana to be smaller Whitlock. "Elect" and "Whitlock" should be the focus.
• at the bottom in a box "Paid for by the Committee to Elect Dana Whitlock"
Nice to have
• it would be good to have her logo as well.
• blue color for democrats and on a white background
Should not have
• pink color

```html
<!DOCTYPE html>
<html lang="en">
<head>
<meta charset="utf-8">
<title>Elect Dana Whitlock for Sheriff – Yard Sign</title>
<link rel="stylesheet" href="https://fonts.googleapis.com/css2?family=Montserrat:wght@600;800;900&display=swap">
<style>
  :root {
    --blue: #3276b5;
    --blue-light: #34a7d7;
    --white: #ffffff;
    --star-ghost: #e9ebee;
    --backdrop: #e6e6e6;
    --gold: #c9a23a;
    --photo-dark: #1f2433;
    --photo-mid: #6b5a55;
  }
  * { margin: 0; padding: 0; box-sizing: border-box; }
  html, body {
    width: 1200px; height: 901px; overflow: hidden;
    background: var(--backdrop);
    font-family: "Montserrat", Arial, sans-serif;
  }
  .yard-sign {
    position: absolute; left: 50px; top: 151px;
    width: 1100px; height: 598px;
    background: var(--white);
    overflow: hidden;
    box-shadow: 0 4px 14px rgba(0,0,0,.18);
  }
  .sign-backdrop { position: absolute; inset: 0; }
  .headline {
    position: absolute; left: 62px; top: 0; width: 645px; height: 186px;
    display: flex; align-items: center; justify-content: space-between;
  }
  .headline-word {
    color: var(--white); font-weight: 900; font-size: 128px;
    line-height: 1; letter-spacing: -2px;
  }
  .badge-star { width: 88px; height: 88px; }
  .candidate-first {
    position: absolute; left: 0; width: 770px; top: 204px;
    text-align: center; color: var(--blue);
    font-weight: 800; font-size: 90px; line-height: 1; letter-spacing: 1px;
  }
  .candidate-last {
    position: absolute; left: 0; width: 770px; top: 290px;
    text-align: center; color: var(--blue);
    font-weight: 900; font-size: 112px; line-height: 1; letter-spacing: -1px;
  }
  .star-row { position: absolute; left: 58px; top: 432px; width: 645px; height: 28px; }
  .campaign-mark {
    position: absolute; left: 50px; top: 470px; width: 106px;
    display: flex; flex-direction: column; align-items: center; gap: 6px;
  }
  .campaign-mark-dot {
    width: 62px; height: 62px; border-radius: 50%; background: var(--gold);
  }
  .campaign-mark-name {
    color: var(--blue); font-weight: 800; font-size: 11px;
    text-align: center; line-height: 1.15; text-transform: uppercase;
  }
  .office-tag {
    position: absolute; left: 179px; top: 476px; width: 411px; height: 60px;
    display: flex; align-items: center; justify-content: center;
  }
  .office-tag-shape { position: absolute; inset: 0; }
  .office-tag-text {
    position: relative; color: var(--white);
    font-weight: 800; font-size: 44px; letter-spacing: 0.5px;
  }
  .disclaimer {
    position: absolute; left: 269px; top: 551px; width: 420px;
    color: var(--blue); font-weight: 600; font-size: 13.5px;
    text-transform: uppercase; white-space: nowrap;
  }
  .candidate-photo {
    position: absolute; left: 746px; top: 42px; width: 354px; height: 556px;
    background: linear-gradient(180deg, var(--photo-mid) 0%, #8d7467 28%, var(--photo-dark) 45%, var(--photo-dark) 100%);
    border-radius: 150px 150px 0 0;
  }
</style>
</head>
<body>
  <main class="yard-sign">
    <svg class="sign-backdrop" width="1100" height="598" viewBox="0 0 1100 598" aria-hidden="true">
      <defs>
        <symbol id="star-shape" viewBox="-1 -1 2 2">
          <polygon points="0,-1 0.2245,-0.309 0.951,-0.309 0.363,0.118 0.588,0.809 0,0.382 -0.588,0.809 -0.363,0.118 -0.951,-0.309 -0.2245,-0.309"/>
        </symbol>
        <clipPath id="band-clip"><rect x="0" y="0" width="1100" height="186"/></clipPath>
      </defs>
      <rect width="1100" height="598" fill="var(--white)"/>
      <g fill="var(--star-ghost)">
        <use href="#star-shape" x="20" y="-20" width="620" height="620"/>
        <use href="#star-shape" x="640" y="-90" width="520" height="520"/>
      </g>
      <rect width="1100" height="186" fill="var(--blue)"/>
      <g fill="var(--white)" opacity="0.09" clip-path="url(#band-clip)">
        <use href="#star-shape" x="20" y="-20" width="620" height="620"/>
        <use href="#star-shape" x="640" y="-90" width="520" height="520"/>
      </g>
    </svg>

    <header class="headline">
      <svg class="badge-star" viewBox="-1.1 -1.1 2.2 2.2" aria-hidden="true" fill="var(--white)">
        <polygon points="0,-0.9 0.2,-0.28 0.856,-0.28 0.33,0.106 0.53,0.728 0,0.344 -0.53,0.728 -0.33,0.106 -0.856,-0.28 -0.2,-0.28"/>
        <circle cx="0" cy="-0.95" r="0.08"/><circle cx="0.9" cy="-0.29" r="0.08"/>
        <circle cx="0.56" cy="0.77" r="0.08"/><circle cx="-0.56" cy="0.77" r="0.08"/>
        <circle cx="-0.9" cy="-0.29" r="0.08"/>
      </svg>
      <span class="headline-word">ELECT</span>
      <svg class="badge-star" viewBox="-1.1 -1.1 2.2 2.2" aria-hidden="true" fill="var(--white)">
        <polygon points="0,-0.9 0.2,-0.28 0.856,-0.28 0.33,0.106 0.53,0.728 0,0.344 -0.53,0.728 -0.33,0.106 -0.856,-0.28 -0.2,-0.28"/>
        <circle cx="0" cy="-0.95" r="0.08"/><circle cx="0.9" cy="-0.29" r="0.08"/>
        <circle cx="0.56" cy="0.77" r="0.08"/><circle cx="-0.56" cy="0.77" r="0.08"/>
        <circle cx="-0.9" cy="-0.29" r="0.08"/>
      </svg>
    </header>

    <h1>
      <span class="candidate-first">DANA</span>
      <span class="candidate-last">WHITLOCK</span>
    </h1>

    <svg class="star-row" viewBox="0 0 645 28" aria-hidden="true" fill="var(--blue)">
      <use href="#star-shape" x="0" y="0" width="28" height="28"/>
      <use href="#star-shape" x="47" y="0" width="28" height="28"/>
      <use href="#star-shape" x="94" y="0" width="28" height="28"/>
      <use href="#star-shape" x="141" y="0" width="28" height="28"/>
      <use href="#star-shape" x="188" y="0" width="28" height="28"/>
      <use href="#star-shape" x="235" y="0" width="28" height="28"/>
      <use href="#star-shape" x="282" y="0" width="28" height="28"/>
      <use href="#star-shape" x="329" y="0" width="28" height="28"/>
      <use href="#star-shape" x="376" y="0" width="28" height="28"/>
      <use href="#star-shape" x="423" y="0" width="28" height="28"/>
      <use href="#star-shape" x="470" y="0" width="28" height="28"/>
      <use href="#star-shape" x="517" y="0" width="28" height="28"/>
      <use href="#star-shape" x="564" y="0" width="28" height="28"/>
      <use href="#star-shape" x="611" y="0" width="28" height="28"/>
    </svg>

    <div class="campaign-mark">
      <span class="campaign-mark-dot"></span>
      <span class="campaign-mark-name">Whitlock for Sheriff</span>
    </div>

    <div class="office-tag">
      <svg class="office-tag-shape" viewBox="0 0 411 60" preserveAspectRatio="none" aria-hidden="true">
        <polygon points="14,0 411,0 397,60 0,60" fill="var(--blue)"/>
      </svg>
      <span class="office-tag-text">FOR SHERIFF</span>
    </div>

    <p class="disclaimer">Paid for by the Committee to Elect Dana Whitlock</p>

    <div class="candidate-photo" role="img" aria-label="Portrait photo of candidate Dana Whitlock in a dark blazer"></div>
  </main>
</body>
</html>
```